BVX2014 Brochure

TRQN needs a design for a brochure cover and inside page for our annual users' conference to take place in January 2014. Every year, we host a popular users group meeting where 800 - 1,000 of our customers attend a 3-day meeting in Houston TX to learn how to more effectively use our software, network with industry peers, and provide feedback on future changes to the software. The goal of the brochure is to get our customers excited about next year's BVXs, and to sell out the events. (An example of last year's brochure is attached. We are not necessarily looking for something similar. It's just to give you an idea of what kind of content is in the brochure.)

The name of the event is 2014 Client Field Summit (also known as BVX).

Theme - the theme of this year's meeting is "Where Innovative Software Meets Real-World Application."

Over 90% of our market are males. They are mainly C-level or managers in construction companies. Our software includes estimating, field entry and reporting, dispatching and scheduling, equipment maintenance management, fuel management, safety management, GPS tracking, and mobile apps. Our corporate color is green, specifically PMS356.

TRQN Brand personality traits - Innovative, market leader, competent, professional, masculine, friendly, and helpful. We've been in business for 28 years, and we are known for our world-class customer support and friendly helpful employees.

Target Market(s)

Construction company executives, estimators, project managers, equipment managers, and IT support. 90% male. We mainly target US and Canadian customers.

Industry/Entity Type

Group

Requirements
Must have
• It needs to be very clear (i.e. probably larger) that this is our 2014 Client Field Summit, and the theme of this year's meeting "Where Innovative Software Meets Real-World Application" needs to be prominent. The meeting name, theme, and our company logo should be prominent.
• Brochure title - 2014 Client Field Summits
• Location - Houston, TX
• Dates - Jan 29 - 31 and Feb 20 - 22 (we host the same meeting twice, but have 1 brochure and registration site)
• Theme - Where Innovative Software Meets Real-World Application
• Logo - we want our logo (TRQN Bold Tools for the Building Trades) to be prominent & should not be altered from the attached image
• Register Today! call to action pointing people to our registration site at www.trqn-example.com/BVX
• Colors - We want our green (PMS 356) to be the dominant color
• Pictures - we want at least 1 picture from past events showing that the meetings are popular, helpful, collaborative and fun.
• Company info on back cover - TRQN, 48207 E. Pelham Rd. Marlow Creek, TX 77592, 800-555-0147, www.trqn-example.com
Nice to have
• When customers view the brochure, we want them to get the following feelings:
• - Professional meeting
• - Innovative technologies
• - New mobile applications on tablets and smartphones
• - Helpful, where they can learn tips and best practices
• - Fun
• Even if they don't attend the meeting, we want everyone who receives the brochure to get a positive feeling about our company.
Should not have
• Feminine design - our industry is largely male construction professionals.
• Don't use script or other goofy fonts
• Logo that is so small it is unreadable
• Too much text
• A design that doesn't project a professional or innovative image

```html
<!DOCTYPE html>
<html lang="en">
<head>
<meta charset="utf-8">
<title>TRQN 2014 Client Field Summit – Brochure Cover</title>
<link href="https://fonts.googleapis.com/css2?family=Questrial&display=swap" rel="stylesheet">
<style>
  :root {
    --canvas-bg: #ffffff;
    --red-deep: #5a0a0e;
    --red-mid: #9e1219;
    --red-bright: #c41a22;
    --band-grey: #3b3736;
    --photo-light: #9a9a9a;
    --photo-dark: #2b2b2b;
    --brand-green: #007a3d;
    --text-white: #ffffff;
  }
  html, body {
    margin: 0;
    padding: 0;
    width: 1200px;
    height: 1000px;
    overflow: hidden;
    background: var(--canvas-bg);
  }
  .canvas {
    position: relative;
    width: 1200px;
    height: 1000px;
  }
  .cover {
    position: absolute;
    left: 0;
    top: 0;
    width: 1200px;
    height: 1000px;
    display: block;
  }
  .cover-text {
    font-family: "Questrial", "Century Gothic", sans-serif;
    fill: var(--text-white);
  }
  .brand-name {
    font-family: "Questrial", "Century Gothic", sans-serif;
    fill: var(--brand-green);
    font-size: 46px;
    letter-spacing: 2px;
  }
  .theme-line { font-size: 30px; letter-spacing: 0.5px; }
  .event-year { font-size: 120px; }
  .event-name { font-size: 34px; }
</style>
</head>
<body>
<main class="canvas">
  <svg class="cover" viewBox="0 0 1200 1000" xmlns="http://www.w3.org/2000/svg">
    <defs>
      <radialGradient id="redField" cx="0.4" cy="0.45" r="0.75">
        <stop offset="0" stop-color="var(--red-bright)"/>
        <stop offset="0.55" stop-color="var(--red-mid)"/>
        <stop offset="1" stop-color="var(--red-deep)"/>
      </radialGradient>
      <radialGradient id="redShadow" cx="0.85" cy="0.35" r="0.5">
        <stop offset="0" stop-color="#3a0508" stop-opacity="0.7"/>
        <stop offset="1" stop-color="#3a0508" stop-opacity="0"/>
      </radialGradient>
      <linearGradient id="photoTone" x1="0" y1="0" x2="1" y2="1">
        <stop offset="0" stop-color="var(--photo-light)"/>
        <stop offset="0.6" stop-color="#5a5a5a"/>
        <stop offset="1" stop-color="var(--photo-dark)"/>
      </linearGradient>
      <clipPath id="pageClip">
        <rect x="236" y="0" width="709" height="1000"/>
      </clipPath>
    </defs>

    <g class="page" clip-path="url(#pageClip)">
      <rect class="page-background" x="236" y="0" width="709" height="1000" fill="url(#redField)"/>
      <rect class="page-shade" x="236" y="0" width="709" height="1000" fill="url(#redShadow)"/>

      <polygon class="event-photo" role="img"
        aria-label="Black-and-white photo of a large audience seated at a conference session"
        points="445,0 945,0 945,242 556,356"
        fill="url(#photoTone)"/>

      <g class="grid-bands" stroke="var(--band-grey)" stroke-width="18" fill="none">
        <line x1="430" y1="0" x2="745" y2="1000"/>
        <line x1="236" y1="460" x2="945" y2="250"/>
      </g>

      <g class="brand-mark" transform="rotate(-16.5 262 410)">
        <rect x="262" y="372" width="34" height="34" fill="var(--brand-green)"/>
        <text class="brand-name" x="306" y="406">TRQN</text>
      </g>

      <g class="theme cover-text" transform="rotate(-16.5 585 415)">
        <text class="theme-line" x="585" y="415">Where Innovative</text>
        <text class="theme-line" x="585" y="452">Software Meets</text>
        <text class="theme-line" x="585" y="489">Real-World Application</text>
      </g>

      <g class="event-title cover-text" transform="rotate(-16.5 372 840)">
        <text class="event-year" x="372" y="840">2014</text>
        <text class="event-name" x="352" y="880">Client Field Summit</text>
      </g>
    </g>
  </svg>
</main>
</body>
</html>
```